URGENT REQUEST Business Card for Executive Coach (already have logo)

Tavener Growth Advisory is a one person business doing high-end executive coaching, leadership training, and personal transformation work (psychotherapy). I urgently need new cards to fit my new logo.

I would like the card to be scannable by ScanTile and Quillbook Howdy.

A draft of the company website is at http://pruvex.net/demo/tavener

Target Market(s)

Senior corporate executives

Industry/Entity Type

Leadership

Requirements
Must have

• 1. Please use the company tag line: "Clear thinking for senior leadership growth"
2. My name is: Gregory Tavener, PhD (Kelbrook)
3. Behind my name, please make "(Kelbrook)" in smaller font.
4. My Title: Executive Coach & Leadership Trainer
4. No street address
5. If there is space, please put my current appointments:
Leadership Studies Faculty (CPA)
Supervisor & Coach (VORTEK)
6. Email: Gtavgreg@TavenerAdvisory.net
7. Web: www.TavenerAdvisory.net
8. Mobile: +65 8456-0000
Nice to have
• Company Tag Line:
• Clear thinking for senior leadership growth and personal transformation
• What I provide:
• Executive Coaching
• Leadership Training
• Personal Transformation

```html
<!DOCTYPE html>
<html lang="en">
<head>
<meta charset="utf-8">
<title>Tavener Growth Advisory – Business Card Front</title>
<link rel="stylesheet" href="https://fonts.googleapis.com/css2?family=Open+Sans:wght@400;600;700&display=swap">
<style>
  :root {
    --card-red: #8e171c;
    --card-red-soft: #971d22;
    --ink-white: #ffffff;
    --ink-cream: #f6ecea;
  }
  * { margin: 0; padding: 0; box-sizing: border-box; }
  html, body {
    width: 1200px;
    height: 734px;
    overflow: hidden;
    background: var(--card-red);
  }
  .card-front {
    position: relative;
    width: 1200px;
    height: 734px;
    overflow: hidden;
    font-family: "Open Sans", Arial, sans-serif;
    color: var(--ink-white);
  }
  .card-backdrop {
    position: absolute;
    inset: 0;
    background: radial-gradient(ellipse at 50% 45%, var(--card-red-soft) 0%, var(--card-red) 70%);
  }
  .brand-block {
    position: absolute;
    left: 0;
    right: 0;
    top: 282px;
    text-align: center;
  }
  .brand-name {
    display: inline-flex;
    align-items: center;
    gap: 20px;
    font-weight: 600;
    font-size: 56px;
    line-height: 1.1;
    letter-spacing: 1px;
    color: var(--ink-cream);
  }
  .brand-dot {
    width: 20px;
    height: 20px;
    border-radius: 50%;
    background: var(--ink-cream);
    flex: none;
  }
  .tagline {
    position: absolute;
    left: 0;
    right: 0;
    top: 420px;
    text-align: center;
    font-weight: 600;
    font-size: 22px;
    letter-spacing: 0.2px;
    color: var(--ink-white);
  }
  .website {
    position: absolute;
    left: 0;
    right: 0;
    top: 628px;
    text-align: center;
    font-weight: 400;
    font-size: 24px;
    letter-spacing: 2.4px;
    color: var(--ink-white);
  }
  .website strong { font-weight: 700; }
</style>
</head>
<body>
  <main class="card-front">
    <div class="card-backdrop" role="img" aria-label="Faint pattern of scattered circles on a deep red background"></div>

    <div class="brand-block">
      <h1 class="brand-name"><span class="brand-dot" aria-hidden="true"></span>Tavener Growth Advisory</h1>
    </div>

    <p class="tagline">Clear thinking for senior leadership growth</p>

    <p class="website">www.<strong>TavenerAdvisory</strong>.net</p>
  </main>
</body>
</html>
```